A label for a bottle of Gin that reflect the area in which it is made - Farrow

I have attached a couple of labels that we are not very happy with. We are looking for something that portrays a premium brand. The bottle is called Verbelle 700ml. and the image should be max 9cm by 7cm. For details on webpage - see notes at quellon.co.uk/farrow and quellon.co.uk/farrowgin. The website should just be a single homepage with a link to quellon.co.uk/farrowgin

The words "Small Batch Handmade Gin" could feature

Number of Pages Required

1 page

Requirements
Nice to have
• Gold or Silver that can add to overall quality feel of the label.
Should not have
• Transparent labels look great when back lit but tend to disappear when on a dark bar with other brighter bottles. Avoid transparency

```html
<!DOCTYPE html>
<html lang="en">
<head>
<meta charset="UTF-8">
<title>Farrow Gin – Label</title>
<link rel="stylesheet" href="https://fonts.googleapis.com/css2?family=Montserrat:wght@300;400;600&display=swap">
<style>
  :root {
    --canvas: #ffffff;
    --label-paper: #ffffff;
    --map-light: #f6f6f7;
    --map-mid: #e6e7e9;
    --silver-light: #e9eaec;
    --silver-dark: #a9acb1;
    --ink: #1b1b1b;
    --grey-text: #8d8f93;
    --orange: #f08a1c;
    --orange-deep: #ee6f0c;
    --band-text: #ffffff;
    --band-small: #ffd84a;
  }
  * { margin: 0; padding: 0; box-sizing: border-box; }
  html, body {
    width: 1200px;
    height: 1000px;
    overflow: hidden;
    background: var(--canvas);
    font-family: "Montserrat", sans-serif;
  }
  .canvas {
    position: relative;
    width: 1200px;
    height: 1000px;
  }
  .label {
    position: absolute;
    left: 197px;
    top: 250px;
    width: 806px;
    height: 638px;
    background: var(--label-paper);
    box-shadow: 0 10px 40px rgba(0, 0, 0, 0.08);
  }
  .label__map {
    position: absolute;
    inset: 0;
    background:
      linear-gradient(115deg, var(--map-light) 0%, var(--map-mid) 35%, var(--label-paper) 55%, var(--map-mid) 80%, var(--map-light) 100%);
  }
  .label__rule {
    position: absolute;
    left: 0;
    width: 100%;
    height: 7px;
    background: linear-gradient(90deg, var(--silver-light), var(--silver-dark) 50%, var(--silver-light));
  }
  .label__rule--top { top: 0; }
  .label__rule--bottom { bottom: 0; }
  .brand-disc {
    position: absolute;
    left: 50%;
    top: -122px;
    width: 241px;
    height: 241px;
    margin-left: -120.5px;
    border-radius: 50%;
    background: var(--orange);
  }
  .brand-name {
    position: absolute;
    left: 0;
    width: 100%;
    top: 193px;
    text-align: center;
    font-weight: 600;
    font-size: 106px;
    letter-spacing: 0.12em;
    padding-left: 0.12em;
    color: var(--ink);
    line-height: 1;
  }
  .product-type {
    position: absolute;
    left: 0;
    width: 100%;
    top: 348px;
    text-align: center;
    font-weight: 300;
    font-size: 50px;
    letter-spacing: 0.75em;
    padding-left: 0.75em;
    color: var(--grey-text);
    line-height: 1;
  }
  .info-band {
    position: absolute;
    left: 105px;
    top: 570px;
    width: 596px;
    height: 136px;
    background: linear-gradient(90deg, var(--orange), var(--orange-deep));
    display: flex;
    align-items: center;
    justify-content: space-between;
    padding: 0 48px;
    color: var(--band-text);
  }
  .info-band__tagline {
    text-align: center;
    font-weight: 400;
    font-size: 37px;
    letter-spacing: 0.06em;
    line-height: 1.25;
  }
  .info-band__spec {
    text-align: center;
    color: var(--band-small);
    line-height: 1.1;
  }
  .info-band__value {
    display: block;
    font-weight: 600;
    font-size: 22px;
  }
  .info-band__unit {
    display: block;
    font-weight: 300;
    font-size: 13px;
    letter-spacing: 0.1em;
  }
</style>
</head>
<body>
  <main class="canvas">
    <section class="label">
      <div class="label__map" role="img" aria-label="Faint engraved map of the Farrow peninsula and coastline"></div>
      <div class="label__rule label__rule--top"></div>
      <div class="label__rule label__rule--bottom"></div>
      <div class="brand-disc" aria-hidden="true"></div>
      <h1 class="brand-name">FARROW</h1>
      <p class="product-type">GIN</p>
      <div class="info-band">
        <p class="info-band__spec"><span class="info-band__value">70</span><span class="info-band__unit">CL</span></p>
        <p class="info-band__tagline">SMALL BATCH<br>BRITISH GIN</p>
        <p class="info-band__spec"><span class="info-band__value">42%</span><span class="info-band__unit">VOL</span></p>
      </div>
    </section>
  </main>
</body>
</html>
```